Guaranteed Job - Sleek Sexy Business Card UV Spot

Im looking for a sleek and sexy business card, that resembles elite or VIP status status.
our business is corinvale.example
you can view our products on there, but our main audience for handing out our cards will be for people in the hospitality industry, so it will need to impress high management and CEO of hotels and restaurants, bars, clubs etc...
the card features will have UV spot on both sides, 400gsm stock. standard size.
Artwork should be 86 x 54mm + 2mm bleed = 90 x 58mm
it should have a nice "unique" uv spot pattern that highlights the card, not a repeated pattern, theres no originality there, and it will be disregarded.
The written material will be:
Corin Vale Hospitality College (logo)
Tobin Marsh
Director
Phone: 1300 615 737
Mobile: 0455 817 296
Email: info@corinvale.example
website: www.corinvale.example
I'm looking for originality here, i don't want just a simple stock card, want something that has a wow factor for people.
You will find the logo attached. you may invert the white to black words to suit the background as you please.
thank you and good luck
As a side note, ive received a lot of proposals, im too busy to give feedback to each and every one, so if i havent provided feedback for your design within 24 hours, then consider it not acceptable, and you could resubmit another design.
So far i have not seen any design that stood out for me, they all seem pretty generic. there nothing thats unique, i would figure for the amount that im offering, that people would put some more effort and creativity into the design.
so far over 200 designs submitted, and nothing i have seen looks very original, everything looks like a different variation of the same stuff, i said it very clearly i wanted something unique, the only thing that has come close to it so far is this one
Reason: Ive received alot of design concepts and i have reviewed everyone, but i havent had time to give feedback to every single one, only the ones that have interested me, if i havent responded, its because i havent found it good enough.
so far only a few design have been on par with what ive been looking for, an attractive eye popping design.
heres a few of them,
http://files.pixelbazaar.example/design_img/51736/62418/62418_2840915_51736_image.jpg
http://files.pixelbazaar.example/design_img/51736/68254/68254_2841377_51736_image.jpg
theyre, both unique and original, and eye catching, the only thing theyre missing is the sexyness.
if you still think you have some creativity left in your minds, then throw it on here.
Reason: Sorry guys for the delay, I was in a serious accident and out of commission for the past few months, I'm just slowly recovering now, please bare with me as i try to attend to this project, it may take me awhile as I have other projects that are on standby, I'm not 100% at the moment, so im extending the deadline for 2 weeks right now. Thanks for your patience.
Hospitality

```html
<!DOCTYPE html>
<html lang="en">
<head>
<meta charset="utf-8">
<title>Corin Vale Hospitality College — Business Card</title>
<link rel="stylesheet" href="https://fonts.googleapis.com/css2?family=Barlow:wght@500;600&family=Arimo:wght@400;700&display=swap">
<style>
  :root {
    --stage: #d9d9d9;
    --card-dark: #2b2b2b;
    --card-dark-edge: #3a3a3a;
    --sky: #6fb3e6;
    --sky-light: #8fd6ff;
    --sky-deep: #4f94cc;
    --ink: #151515;
    --paper: #ffffff;
    --muted: #8a8a8a;
  }
  * { box-sizing: border-box; margin: 0; padding: 0; }
  html, body { width: 1200px; height: 900px; overflow: hidden; }
  body {
    background: var(--stage);
    position: relative;
    font-family: "Arimo", Arial, sans-serif;
  }
  .card {
    position: absolute;
    width: 580px;
    height: 374px;
    overflow: hidden;
    box-shadow: 0 14px 30px rgba(0,0,0,.28);
  }
  .card svg.card-art { position: absolute; inset: 0; width: 100%; height: 100%; }

  /* Front */
  .card-front { left: 80px; top: 60px; background: var(--card-dark); }
  .front-brand {
    position: absolute;
    left: 70px;
    top: 140px;
    display: flex;
    align-items: center;
    gap: 18px;
  }
  .brand-square {
    width: 62px; height: 62px;
    background: var(--sky);
  }
  .brand-name {
    font-family: "Barlow", Arial, sans-serif;
    font-weight: 600;
    color: var(--sky);
    text-transform: uppercase;
    font-size: 26px;
    line-height: 1.1;
    letter-spacing: .5px;
  }

  /* Back */
  .card-back { left: 540px; top: 470px; background: var(--sky); }
  .back-brand {
    position: absolute;
    left: 150px;
    top: 18px;
    font-family: "Barlow", Arial, sans-serif;
    font-weight: 600;
    color: var(--ink);
    text-transform: uppercase;
    font-size: 15px;
    line-height: 1.1;
  }
  .contact-list {
    position: absolute;
    left: 40px;
    top: 150px;
    display: grid;
    grid-template-columns: 80px auto;
    row-gap: 2px;
    color: var(--ink);
  }
  .contact-label { font-size: 16px; line-height: 22px; }
  .contact-value { font-size: 21px; line-height: 22px; color: var(--paper); }
  .person {
    position: absolute;
    right: 34px;
    top: 70px;
    text-align: right;
    color: var(--paper);
    font-weight: 700;
  }
  .person-name { font-size: 20px; }
  .person-role { font-size: 13px; }
</style>
</head>
<body>

  <section class="card card-front" aria-label="Card front">
    <svg class="card-art" viewBox="0 0 580 374" preserveAspectRatio="none">
      <defs>
        <linearGradient id="uvBand" x1="0" y1="0" x2="1" y2="1">
          <stop offset="0" stop-color="#8ac3ee"/>
          <stop offset=".5" stop-color="#5a9fd4"/>
          <stop offset="1" stop-color="#7fb8e6"/>
        </linearGradient>
      </defs>
      <rect width="580" height="374" fill="var(--card-dark)"/>
      <polygon points="450,0 580,0 580,374 490,374" fill="url(#uvBand)" role="img" aria-label="Faceted geometric UV spot pattern in blue"/>
    </svg>
    <div class="front-brand">
      <span class="brand-square" aria-hidden="true"></span>
      <p class="brand-name">Corin Vale<br>Hospitality College</p>
    </div>
  </section>

  <section class="card card-back" aria-label="Card back">
    <svg class="card-art" viewBox="0 0 580 374" preserveAspectRatio="none">
      <defs>
        <linearGradient id="skyWash" x1="0" y1="1" x2="1" y2="0">
          <stop offset="0" stop-color="var(--sky-deep)"/>
          <stop offset=".7" stop-color="var(--sky-light)"/>
        </linearGradient>
        <linearGradient id="darkPanel" x1="0" y1="0" x2="0" y2="1">
          <stop offset="0" stop-color="var(--card-dark-edge)"/>
          <stop offset="1" stop-color="var(--card-dark)"/>
        </linearGradient>
      </defs>
      <rect width="580" height="374" fill="url(#skyWash)"/>
      <polygon points="380,0 580,0 580,374 300,374 350,170" fill="url(#darkPanel)"/>
    </svg>
    <p class="back-brand">Corin Vale<br>Hospitality College</p>
    <dl class="contact-list">
      <dt class="contact-label">phone:</dt><dd class="contact-value">1300 615 737</dd>
      <dt class="contact-label">mobile:</dt><dd class="contact-value">0455 817 296</dd>
      <dt class="contact-label">email:</dt><dd class="contact-value">info@corinvale.example</dd>
      <dt class="contact-label">website:</dt><dd class="contact-value">www.corinvale.example</dd>
    </dl>
    <div class="person">
      <p class="person-name">Tobin Marsh</p>
      <p class="person-role">Director</p>
    </div>
  </section>

</body>
</html>
```